Criação de Capa para Facebook para Associações, ONGs ou Comunidades
A empresa queria:
" Fazemos projetos customizados de automação e Home Theater de luxo "

```html
<!DOCTYPE html>
<html lang="pt-BR">
<head>
<meta charset="UTF-8">
<title>Sonaris — Automação e Home Theater</title>
<link href="https://fonts.googleapis.com/css2?family=Montserrat:wght@400;500&display=swap" rel="stylesheet">
<style>
  :root {
    --page-bg: #efefef;
    --brand-dark: #2a2622;
    --room-deep: #1c1a17;
    --room-mid: #4a4036;
    --room-warm: #8a7a66;
    --room-light: #c9bba6;
    --overlay: rgba(22, 20, 18, 0.55);
    --ink-light: #ffffff;
    --gold: #b8955f;
    --rule: rgba(255, 255, 255, 0.55);
  }
  * { margin: 0; padding: 0; box-sizing: border-box; }
  html, body {
    width: 1200px;
    height: 1200px;
    overflow: hidden;
    background: var(--page-bg);
    font-family: "Montserrat", sans-serif;
  }
  .canvas {
    position: relative;
    width: 1200px;
    height: 1200px;
  }

  /* Profile square */
  .profile-tile {
    position: absolute;
    left: 475px;
    top: 168px;
    width: 246px;
    height: 246px;
    background: var(--brand-dark);
    display: flex;
    flex-direction: column;
    align-items: center;
    justify-content: center;
  }
  .profile-tile .brand-name {
    color: var(--ink-light);
    font-weight: 500;
    font-size: 32px;
    letter-spacing: 2px;
    line-height: 1;
  }
  .profile-tile .brand-tagline {
    margin-top: 8px;
    color: var(--gold);
    font-weight: 400;
    font-size: 9px;
    letter-spacing: 3px;
  }

  /* Cover banner */
  .cover {
    position: absolute;
    left: 29px;
    top: 509px;
    width: 1142px;
    height: 422px;
    overflow: hidden;
  }
  .cover-photo {
    position: absolute;
    inset: 0;
    background:
      radial-gradient(ellipse at 30% 45%, var(--room-light) 0%, transparent 40%),
      linear-gradient(90deg, var(--room-warm) 0%, var(--room-mid) 35%, var(--room-deep) 60%, var(--room-mid) 85%, var(--room-deep) 100%);
  }
  .cover-overlay {
    position: absolute;
    inset: 0;
    background: var(--overlay);
  }
  .cover-content {
    position: absolute;
    inset: 0;
    display: flex;
    flex-direction: column;
    align-items: center;
  }
  .cover .brand-name {
    margin-top: 142px;
    color: var(--ink-light);
    font-weight: 500;
    font-size: 70px;
    letter-spacing: 5px;
    line-height: 1;
  }
  .cover .brand-tagline {
    margin-top: 22px;
    color: var(--gold);
    font-weight: 400;
    font-size: 17px;
    letter-spacing: 6px;
  }
  .cover .divider {
    margin-top: 54px;
    width: 480px;
    height: 1px;
    background: var(--rule);
  }
  .contact-row {
    margin-top: 26px;
    display: flex;
    align-items: center;
    gap: 36px;
    color: var(--ink-light);
    font-size: 14px;
    letter-spacing: 1px;
  }
  .contact-item {
    display: flex;
    align-items: center;
    gap: 8px;
  }
  .contact-dot {
    width: 14px;
    height: 14px;
    border: 1.5px solid var(--ink-light);
    border-radius: 50%;
  }
</style>
</head>
<body>
<main class="canvas">

  <section class="profile-tile">
    <div class="brand-name">SONARIS</div>
    <div class="brand-tagline">AUTOMAÇÃO E HOME THEATER</div>
  </section>

  <section class="cover">
    <div class="cover-photo" role="img" aria-label="Sala de home theater de luxo com TV na parede, caixas de som e controle de automação em um smartphone"></div>
    <div class="cover-overlay"></div>
    <div class="cover-content">
      <div class="brand-name">SONARIS</div>
      <div class="brand-tagline">AUTOMAÇÃO E HOME THEATER</div>
      <div class="divider"></div>
      <div class="contact-row">
        <span class="contact-item"><span class="contact-dot"></span>@SONARIS</span>
        <span class="contact-item">WWW.SONARIS.COM.BR</span>
      </div>
    </div>
  </section>

</main>
</body>
</html>
```